Small company security and risk consulting startup needs an explosive message via marketing colla...

Need a two page (front/back) flyer that calls out our three primary service areas incorporating tallyquill developed logo and website visuals. Something that grabs attention at first glance to entice the viewer to read and connect for a services consultation. I will need the ability to make minor adjustments and add language.

```html
<!DOCTYPE html>
<html lang="en">
<head>
<meta charset="utf-8">
<title>BastionCrest – Two Page Flyer</title>
<link href="https://fonts.googleapis.com/css2?family=Bebas+Neue&family=Source+Sans+3:wght@400;600;700&display=swap" rel="stylesheet">
<style>
  :root{
    --red:#c8161d;
    --red-dark:#8e0e13;
    --ink:#1b1b1b;
    --charcoal:#2c2c2c;
    --steel:#b9b9b9;
    --paper:#ffffff;
    --body:#3c3c3c;
    --blue:#1f3f8f;
    --backdrop:#e6e6e6;
    --display:"Bebas Neue", Impact, sans-serif;
    --text:"Source Sans 3", Arial, sans-serif;
  }
  *{box-sizing:border-box;margin:0;padding:0}
  html,body{width:1200px;height:791px;overflow:hidden;background:var(--backdrop)}
  .canvas{position:relative;width:1200px;height:791px}
  .page{position:absolute;top:59px;width:516px;height:668px;background:var(--paper);overflow:hidden;box-shadow:0 4px 14px rgba(0,0,0,.25)}
  .page--front{left:72px}
  .page--back{left:637px}
  .layer{position:absolute;left:0;top:0}
  .brand{position:absolute;left:24px;top:50px;display:flex;align-items:center;gap:8px}
  .brand__mark{width:18px;height:18px;background:var(--red)}
  .brand__name{font-family:var(--text);font-weight:700;font-size:22px;color:var(--red);letter-spacing:.5px}
  .tagline{position:absolute;left:16px;top:164px;font-family:var(--display);font-size:17px;font-weight:400;color:var(--red);letter-spacing:.2px}
  .intro{position:absolute;left:17px;top:199px;font-family:var(--text);font-size:10.5px;line-height:17.7px;color:#fff;white-space:nowrap}
  .section-tab{position:absolute;left:0;height:23px;padding-left:16px;font-family:var(--display);font-size:19px;font-weight:400;line-height:24px;color:#fff;background:linear-gradient(90deg,var(--red-dark),var(--red));clip-path:polygon(0 0,100% 0,92% 100%,0 100%)}
  .copy{position:absolute;left:15px;width:486px;font-family:var(--text);font-size:9.8px;line-height:12.2px;color:var(--body);text-align:justify}
  .service{position:absolute;width:110px;text-align:center;color:#fff;font-family:var(--text)}
  .service__title{font-weight:700;font-size:9.4px;line-height:10.5px}
  .service__note{font-size:6px;line-height:7px;opacity:.75;margin-top:4px}
  .service svg{display:block;margin:0 auto 6px}
  .review{position:absolute;left:12px;top:421px;width:493px;height:155px;background:linear-gradient(180deg,var(--red-dark),#b3121a 40%,var(--red-dark));clip-path:polygon(0 0,50% 3%,100% 0,100% 88%,50% 100%,0 88%);color:#fff;font-family:var(--text);padding:30px 10px 0}
  .review__title{font-size:15.5px;text-align:center;font-weight:400}
  .review__body{margin-top:10px;font-size:8.8px;line-height:11.1px;text-align:justify;font-weight:400}
  .contact{position:absolute;left:16px;top:607px;font-family:var(--text);font-size:9.2px;line-height:13.4px;color:#fff;list-style:none}
  .contact li{display:flex;align-items:center;gap:6px}
  .contact__icon{width:10px;height:10px;background:var(--red);border-radius:2px;display:flex;align-items:center;justify-content:center}
  .social{position:absolute;left:386px;top:646px;display:flex;gap:12px}
  .social span{width:15px;height:15px;border:1.2px solid #fff;border-radius:50%}
  .badge{position:absolute;left:439px;top:567px;width:62px;height:62px;border-radius:50%;background:#fff;border:3px solid var(--blue);box-shadow:inset 0 0 0 6px #fff,inset 0 0 0 8px var(--red)}
  .photo{fill:url(#photoTone)}
</style>
</head>
<body>
<div class="canvas">

  <section class="page page--front">
    <svg class="layer" width="516" height="668" viewBox="0 0 516 668">
      <defs>
        <linearGradient id="bandTone" x1="0" y1="0" x2="0" y2="1">
          <stop offset="0" stop-color="#111"/><stop offset=".55" stop-color="#3a3a3a"/><stop offset="1" stop-color="#1a1a1a"/>
        </linearGradient>
        <linearGradient id="photoTone" x1="0" y1="0" x2="1" y2="1">
          <stop offset="0" stop-color="#5a5a5a"/><stop offset=".5" stop-color="#2d2d2d"/><stop offset="1" stop-color="#6b6b6b"/>
        </linearGradient>
        <linearGradient id="footTone" x1="0" y1="0" x2="1" y2="0">
          <stop offset="0" stop-color="#161616"/><stop offset=".5" stop-color="#3a3a3a"/><stop offset="1" stop-color="#161616"/>
        </linearGradient>
      </defs>
      <rect x="0" y="114" width="516" height="180" fill="url(#bandTone)"/>
      <polygon points="340,0 516,0 516,336 400,336 256,164" fill="var(--steel)"/>
      <polygon points="352,0 516,0 516,330 406,330 266,164" fill="var(--red)"/>
      <polygon points="362,3 516,3 516,324 411,324 276,164" fill="#222"/>
      <polygon class="photo" role="img" aria-label="Photo of a presenter in a suit speaking to an audience in a conference room" points="366,6 516,6 516,320 413,320 280,164"/>
      <polygon points="0,428 96,428 40,558 0,558" fill="#e4e4e4"/>
      <polygon points="470,428 516,428 516,558 500,558" fill="#e4e4e4"/>
      <polygon points="93,428 156,428 219,558 30,558" fill="var(--charcoal)"/>
      <polygon points="161,428 346,428 283,558 222,558" fill="var(--red)"/>
      <polygon points="224,558 283,558 346,428 320,428" fill="var(--red-dark)" opacity=".5"/>
      <polygon points="359,428 412,428 472,558 286,558" fill="var(--blue)"/>
      <polygon points="0,582 290,612 516,628 516,668 0,668" fill="url(#footTone)"/>
      <polygon points="290,612 516,588 516,628" fill="var(--red)"/>
    </svg>

    <div class="brand"><span class="brand__mark"></span><span class="brand__name">BastionCrest</span></div>
    <h2 class="tagline">Commitment - Integrity - Results</h2>
    <p class="intro">National security is the requirement to maintain the<br>survival of the state through the use of economic power,<br>diplomacy, power projection and political power.</p>

    <h3 class="section-tab" style="top:313px;width:138px">About Us</h3>
    <p class="copy" style="top:348px">Nunc tempus felis vitae urna Vivamus porttitor neque at volutpat rutrum purus nisieleifend libero a tempus libero lectus feugiat felis Morbi diam mauris viverra in gravida eu mattis in ante Morbi eget arcu Morbi porta libero id ullamcorper nonummy nibh ligula pulvinar metus eget consectetuer augue nisi quis lacus Ut ac mi quis lacus mollis aliquam Curabitur iacults Nunc tempus felis vitae urna Vivamus porttitor neque at volutpat rutrum purus nisieleifend</p>

    <div class="service" style="left:71px;top:448px">
      <svg width="28" height="26" viewBox="0 0 28 26" fill="none" stroke="#fff" stroke-width="1.5"><rect x="2" y="2" width="24" height="16" rx="1"/><path d="M8 10c3-4 9-4 12 0c-3 4-9 4-12 0z"/><circle cx="14" cy="10" r="1.8"/><path d="M10 24h8M14 18v6"/></svg>
      <div class="service__title">NATIONAL<br>SECURITY</div>
      <div class="service__note">Morbi diam mauris viverra in gravida eu mattis in an</div>
    </div>
    <div class="service" style="left:198px;top:446px">
      <svg width="28" height="28" viewBox="0 0 28 28" fill="none" stroke="#fff" stroke-width="1.5"><circle cx="14" cy="12" r="8"/><circle cx="14" cy="12" r="3"/><path d="M14 2v3M14 19v3M4 12h3M21 12h3M10 22h8v4h-8z"/></svg>
      <div class="service__title">RISK MANAGEMENT<br>SERVICES</div>
      <div class="service__note">Morbi diam mauris viverra in gravida eu mattis in an</div>
    </div>
    <div class="service" style="left:326px;top:446px">
      <svg width="28" height="28" viewBox="0 0 28 28" fill="none" stroke="#fff" stroke-width="1.5"><rect x="3" y="3" width="12" height="9" rx="1"/><rect x="13" y="9" width="12" height="9" rx="1"/><circle cx="9" cy="20" r="2.5"/><path d="M4 27c0-3 2-4 5-4s5 1 5 4"/></svg>
      <div class="service__title">CONSULTING<br>SERVICES</div>
      <div class="service__note">Morbi diam mauris viverra in gravida eu mattis in an</div>
    </div>

    <div class="badge" role="img" aria-label="Certification badge"></div>
    <ul class="contact">
      <li><span class="contact__icon"><svg width="7" height="7" viewBox="0 0 8 8"><path d="M1 1h2l1 2-1 1c.5 1 1 1.5 2 2l1-1 2 1v2C4 8 0 4 1 1z" fill="#fff"/></svg></span>(555) 318 4470</li>
      <li><span class="contact__icon"><svg width="7" height="6" viewBox="0 0 8 6" fill="none" stroke="#fff"><rect x=".5" y=".5" width="7" height="5"/><path d="M.5 .5l3.5 3 3.5-3"/></svg></span>info@bastioncrest.com</li>
      <li><span class="contact__icon"><svg width="7" height="7" viewBox="0 0 8 8" fill="none" stroke="#fff"><circle cx="4" cy="4" r="3.3"/><path d="M.7 4h6.6M4 .7v6.6"/></svg></span>www.bastioncrest.com</li>
      <li><span class="contact__icon"><svg width="6" height="8" viewBox="0 0 6 8"><path d="M3 8C1 5 0 4 0 3a3 3 0 016 0c0 1-1 2-3 5z" fill="#fff"/></svg></span>42 Ridgeline Ave # Suite 5 Austin TX 78701</li>
    </ul>
    <div class="social"><span></span><span></span><span></span><span></span></div>
  </section>

  <section class="page page--back">
    <svg class="layer" width="516" height="668" viewBox="0 0 516 668">
      <defs>
        <linearGradient id="deskTone" x1="0" y1="0" x2="1" y2="1">
          <stop offset="0" stop-color="#c9c2b6"/><stop offset=".45" stop-color="#5d6064"/><stop offset="1" stop-color="#9aa0a6"/>
        </linearGradient>
        <linearGradient id="footTone2" x1="0" y1="0" x2="1" y2="0">
          <stop offset="0" stop-color="#161616"/><stop offset=".5" stop-color="#3a3a3a"/><stop offset="1" stop-color="#161616"/>
        </linearGradient>
      </defs>
      <polygon points="0,238 253,282 516,226 516,240 253,298 0,256" fill="var(--red)"/>
      <polygon points="0,0 516,0 516,226 253,282 0,238" fill="url(#deskTone)" role="img" aria-label="Photo of hands using a laptop, smartphone and tablet showing security dashboards"/>
      <line x1="0" y1="317" x2="516" y2="317" stroke="#ddd"/>
      <polygon points="0,582 290,612 516,628 516,668 0,668" fill="url(#footTone2)"/>
      <polygon points="290,612 516,588 516,628" fill="var(--red)"/>
    </svg>

    <h3 class="section-tab" style="top:294px;width:137px">Who We Are</h3>
    <p class="copy" style="top:330px;line-height:12.3px">Nunc tempus felis vitae urna Vivamus porttitor neque at volutpat rutrum purus nisieleifend libero a tempus libero lectus feugiat felis Morbi diam mauris viverra in gravida eu mattis in ante Morbi eget arcu Morbi porta libero id ullamcorper nonummy nibh ligula pulvinar metus eget consectetuer augue nisi quis lacus Ut ac mi quis lacus mollis aliquam Curabitur iacults Nunc tempus felis vitae urna Vivamus porttitor neque at volutpat rutrum purus nisieleifend libero a tempus libero lectus feugiat felis Morbi diam mauris viverra in gravida eu mattis in ante Morbi eget arcu Morbi porta libero id ullamcorper nonummy nibh ligula pulvinar metus eget consectetuer augue nisi quis lacus Ut ac mi quis lacus mollis aliquam Curabitur iacults</p>

    <div class="review">
      <h2 class="review__title">The decision-making process of Strategic Defence and Security Review</h2>
      <p class="review__body">Nunc tempus felis vitae urna Vivamus porttitor neque at volutpat rutrum purus nisieleifend libero a tempus libero lectus feugiat felis Morbi diam mauris viverra in gravida eu mattis in ante Morbi eget arcu Morbi porta libero id ullamcorper nonummy nibh ligula pulvinar metus eget consectetuer augue nisi quis lacus Ut ac mi quis lacus mollis aliquam Curabitur iacults Nunc tempus felis vitae urna Vivamus porttitor neque at volutpat rutrum purus nisieleifend libero a tempus libero lectus feugiat felis Morbi diam mauris viverra in gravida eu mattis in ante Morbi eget arcu Morbi porta libero id ullamcorper nonummy nibh ligula pulvinar metus eget consectetuer augue nisi quis lacus Ut ac mi quis lacus mollis aliquam Curabitur</p>
    </div>

    <div class="badge" role="img" aria-label="Certification badge"></div>
    <ul class="contact">
      <li><span class="contact__icon"><svg width="7" height="7" viewBox="0 0 8 8"><path d="M1 1h2l1 2-1 1c.5 1 1 1.5 2 2l1-1 2 1v2C4 8 0 4 1 1z" fill="#fff"/></svg></span>(555) 318 4470</li>
      <li><span class="contact__icon"><svg width="7" height="6" viewBox="0 0 8 6" fill="none" stroke="#fff"><rect x=".5" y=".5" width="7" height="5"/><path d="M.5 .5l3.5 3 3.5-3"/></svg></span>info@bastioncrest.com</li>
      <li><span class="contact__icon"><svg width="7" height="7" viewBox="0 0 8 8" fill="none" stroke="#fff"><circle cx="4" cy="4" r="3.3"/><path d="M.7 4h6.6M4 .7v6.6"/></svg></span>www.bastioncrest.com</li>
      <li><span class="contact__icon"><svg width="6" height="8" viewBox="0 0 6 8"><path d="M3 8C1 5 0 4 0 3a3 3 0 016 0c0 1-1 2-3 5z" fill="#fff"/></svg></span>42 Ridgeline Ave # Suite 5 Austin TX 78701</li>
    </ul>
    <div class="social"><span></span><span></span><span></span><span></span></div>
  </section>

</div>
</body>
</html>
```